Corvel Lane

Small ageny public transit advocacy, funding and compliance.
Consulting and lobbying efforts for small public transit agencies and communities exploring public transit opportunities.
Updates

I was interested in a simple line sketch suggesting motion, mobility. The card will be black on white. I would like it to include the bUs ones brief; Advocacy, Funding , and Compliance for small transit agencies.

Reason: I have been traveling and have had limited time to respond. Thank you all for your submit talks.

Industry/Entity Type

Consulting

Contact Information for Business Card

Mark D Loyer
Phone (614) 380-2917
Email markdloyer@vantomail.test

```html
<!DOCTYPE html>
<html lang="en">
<head>
<meta charset="utf-8">
<title>Corvel Lane — Business Card</title>
<link rel="stylesheet" href="https://fonts.googleapis.com/css2?family=Jura:wght@500;700&family=Michroma&display=swap">
<style>
  :root {
    --backdrop: #2b2b2e;
    --card-white: #ffffff;
    --card-black: #050505;
    --ink: #0a0a0a;
    --paper-text: #f2f2f2;
    --rule: #1a1a1a;
  }
  * { margin: 0; padding: 0; box-sizing: border-box; }
  html, body {
    width: 1200px;
    height: 800px;
    overflow: hidden;
    background: var(--backdrop);
  }
  .canvas {
    position: relative;
    width: 1200px;
    height: 800px;
    display: flex;
    align-items: center;
    justify-content: center;
  }
  .business-card {
    position: relative;
    width: 1050px;
    height: 600px;
    background: var(--card-white);
    overflow: hidden;
    box-shadow: 0 12px 40px rgba(0,0,0,0.45);
  }
  .brand {
    position: absolute;
    left: 470px;
    top: 200px;
    display: flex;
    align-items: center;
    gap: 18px;
  }
  .brand-dot {
    width: 62px;
    height: 62px;
    border-radius: 50%;
    background: var(--ink);
  }
  .brand-name {
    font-family: "Jura", sans-serif;
    font-weight: 700;
    font-size: 62px;
    color: var(--ink);
    letter-spacing: 1px;
    line-height: 1;
  }
  .tagline-band {
    position: absolute;
    left: 0;
    top: 296px;
    width: 100%;
    height: 38px;
    border-top: 2px solid var(--rule);
    border-bottom: 2px solid var(--rule);
    display: flex;
    align-items: center;
    justify-content: center;
  }
  .tagline {
    font-family: "Michroma", sans-serif;
    font-size: 17px;
    font-variant: small-caps;
    letter-spacing: 3.2px;
    color: var(--ink);
    white-space: nowrap;
  }
  .contact-panel {
    position: absolute;
    left: 0;
    top: 340px;
    width: 100%;
    height: 260px;
    background: var(--card-black);
  }
  .contact {
    position: absolute;
    left: 520px;
    top: 22px;
    font-family: "Jura", sans-serif;
    font-weight: 500;
    color: var(--paper-text);
  }
  .contact-name {
    font-size: 40px;
    letter-spacing: 1px;
    margin-bottom: 42px;
  }
  .contact-phone {
    font-size: 40px;
    letter-spacing: 2px;
    margin-bottom: 8px;
  }
  .contact-email {
    font-size: 32px;
    letter-spacing: 3px;
  }
</style>
</head>
<body>
  <main class="canvas">
    <article class="business-card">
      <div class="brand">
        <span class="brand-dot" aria-hidden="true"></span>
        <span class="brand-name">Corvel Lane</span>
      </div>
      <div class="tagline-band">
        <p class="tagline">Advocacy, Funding , and Compliance for small transit agencies</p>
      </div>
      <section class="contact-panel">
        <div class="contact">
          <p class="contact-name">Mark D Loyer</p>
          <p class="contact-phone">(614) 380-2917</p>
          <p class="contact-email">markdloyer@vantomail.test</p>
        </div>
      </section>
    </article>
  </main>
</body>
</html>
```